Very basic draft completed. Need someone to apply their creative magic

I am building a new website for my business and looking for a designer to assist me on a part-time basis.

My business is a booking site for classes and lessons. It is essentially a directory service, and needs to conform to a standard web-layout that is easy to navigate and familiar to users (i.e. nothing to creative). The function and structure i have adopted is common amongst sites like qumo, hotel booking services, etc.

The first task on my list is to develop the main page. I have already compiled a draft of the first page using Fireworks (see attached) and am looking for someone to cast their creative magic to this draft while maintaining the general layout of the page. After the main page is developed, I will be looking for the same designer to assist with the rest of the site.

Design wise, I'd like to go for a slightly retro feel
By this I mean a moderately modern page with a spark of retro here and there. If you look at my draft you'll notice that I've used regular font for most text, and retro/old-school fonts for surburb names.

I happy for you to suggest colours, but regular page elements such as web links need to remain standard (i.e links = blue) so that they are familiar and identifiable to my users.

Other points:
1) I don't want the page to be too dark (dark headings, images and borders are fine, but I'd like to maintain white or light backgrounds)

2) Positioning: The Body should be centred, with the Header and Footer extending across the hole screen (as illustrated in my draft)

3) I'm happy if the design includes images from photostock libraries.The Silhoute picture for my draft were choosen because there are hundreds of them, and I can regularly change them on the site - keeping it fresh and new. I'd be very happy if the design incorporate images that could also be place often using photo stock images (i.e. happy to keep silhoutes, but leave it to you to decide what looks best)

Note: I'm happy for you to "copy" art work from any photo stock site, and I will pay for the full quality images when the design is selected.

4) The page Footer needs a lot of attention. It will contain standard Footer links/elements.

5) You are free to do anything to the Header section. It needs to have login/register elements

I'm happy to provide further comments, or review other sites/work to help direct design work.

Hi All,

I've updated the project brief, eliminating many of the requirements and giving you the freedom with design submissions, etc. I've also added the $20 payment for submissions. 
Cheers,
Corwin

Reason: I'm away on holiday and will review your submissions and provide feedback when I get back.

```html
<!DOCTYPE html>
<html lang="en">
<head>
<meta charset="utf-8">
<title>Step Outside – Courses &amp; Activities</title>
<link rel="stylesheet" href="https://fonts.googleapis.com/css2?family=Arimo:wght@400;700&family=Open+Sans:wght@400;600;700&display=swap">
<style>
:root{
  --red:#d9121b;
  --red-dark:#7a1a17;
  --text:#555;
  --grey-bar:#3a3a3a;
  --grey-panel:#e9e9e9;
  --yellow:#f0b400;
  --footer-text:#bbb;
  --link-red:#c8101a;
  --brand-ink:#333;
}
*{box-sizing:border-box;margin:0;padding:0}
html,body{width:1059px;height:1200px;overflow:hidden;background:#fff}
body{font-family:"Open Sans",Arial,sans-serif;color:var(--text)}
.page{position:relative;width:1000px;height:1133px;transform:scale(1.059);transform-origin:0 0}
.abs{position:absolute}

/* header */
.site-header{position:absolute;left:0;top:0;width:1000px;height:105px;background:linear-gradient(#fff,#e6e6e6)}
.brand-mark{left:90px;top:40px;width:22px;height:22px;background:var(--red)}
.brand-name{left:122px;top:34px;font:700 28px Arimo,Arial,sans-serif;color:var(--brand-ink);letter-spacing:-.5px;white-space:nowrap}
.header-art{left:608px;top:10px;width:76px;height:90px;background:linear-gradient(#333,#111);border-radius:30px 30px 8px 8px;opacity:.8}
.location-label{left:695px;top:29px;font:700 11px Arimo,Arial,sans-serif;color:var(--red)}
.location-select{left:695px;top:48px;width:218px;height:26px;background:#333;color:#eee;font:400 10px Arimo,Arial,sans-serif;padding:8px 8px}
.location-select .caret{position:absolute;right:0;top:0;width:28px;height:26px;background:var(--red)}

/* search band */
.search-band{position:absolute;left:0;top:105px;width:1000px;height:163px;background:linear-gradient(#8a2420,#6f1a17)}
.search-title{left:268px;top:117px;font:700 19px "Open Sans",Arial,sans-serif;color:#fff;white-space:nowrap}
.search-title span{color:var(--yellow);text-decoration:underline}
.course-box{left:87px;top:149px;width:173px;height:104px;background:linear-gradient(#fcc21a,#e8740c);overflow:hidden}
.course-box h3{position:absolute;left:10px;top:8px;font:700 10px Arimo,Arial,sans-serif;color:#2b1500}
.course-input{position:absolute;left:8px;top:31px;width:156px;height:26px;background:#4a2a10;color:#eee;font:400 9px Arimo,Arial,sans-serif;padding:8px 7px}
.course-input svg{position:absolute;right:7px;top:6px}
.course-crowd{position:absolute;left:0;top:62px;width:173px;height:42px;background:linear-gradient(#a5500c,#4e2305)}
.filter-panel{left:277px;top:149px;width:636px;height:106px;background:#353535;border:1px solid #555;border-radius:4px}
.field{position:absolute;height:32px;background:linear-gradient(#fafafa,#cfcfcf);border-radius:3px;font:700 11px Arimo,Arial,sans-serif;color:#444;padding:10px 8px}
.panel-divider{left:668px;top:149px;width:1px;height:106px;background:#555}
.day-row{left:285px;top:229px;font-size:9px;color:#bbb;display:flex}
.day-row label{display:flex;align-items:center;margin-right:9px}
.day-row i{display:inline-block;width:10px;height:10px;background:#fff;margin-left:5px;position:relative}
.filter-btn{left:816px;top:212px;width:85px;height:29px;background:linear-gradient(#ffb43a,#e67a05);border-radius:4px;color:#fff;font:700 14px "Open Sans",Arial,sans-serif;padding:5px 0 0 10px}
.filter-btn svg{position:absolute;right:9px;top:7px}

/* sidebar */
.side-head{position:absolute;left:87px;width:173px;height:29px;background:var(--grey-bar);color:#fff;font:600 12px "Open Sans",Arial,sans-serif;padding:6px 6px;white-space:nowrap}
.category-list{left:95px;top:326px;list-style:none;font-size:11px;color:#333}
.category-list li{height:20.3px;display:flex;align-items:center}
.category-list .box{width:8px;height:8px;border:1px solid #777;margin-right:9px;font-size:8px;line-height:6px;text-align:center;color:#333}
.category-list .sub{padding-left:34px;color:#777}
.refine{left:87px;top:641px;width:173px;height:145px;background:var(--grey-panel)}
.refine-label{left:96px;font-size:11.5px;color:#444}
.slider{left:104px;width:138px;height:5px;background:linear-gradient(#aaa,#ddd);border-radius:3px}
.slider b{position:absolute;left:72px;top:-4px;width:13px;height:13px;border-radius:50%;background:#555}

/* listing */
.list-head{left:270px;top:285px;width:643px;height:29px;background:var(--red);color:#fff;font:600 12px "Open Sans",Arial,sans-serif}
.list-head span{position:absolute;top:5px}
.card{position:absolute;left:270px;width:643px;height:124px;border:1px solid #ddd;border-radius:5px;background:linear-gradient(#fff,#f5f5f5)}
.card .photo{position:absolute;left:13px;top:13px;width:98px;height:97px;border:1px solid #bbb}
.card h2{position:absolute;left:123px;top:11px;font:400 11.5px Arimo,Arial,sans-serif;color:#111}
.card p{position:absolute;left:123px;top:30px;width:288px;font:400 8.6px/11.8px Arimo,Arial,sans-serif;color:#555;text-align:justify}
.card .more{position:absolute;left:361px;top:82px;font:400 9px Arimo,Arial,sans-serif;color:var(--link-red)}
.schedule{position:absolute;left:424px;top:0;width:79px;height:122px;background:#e6e6e6;font:400 8.5px/15.2px Arimo,Arial,sans-serif;color:#333;padding:9px 0 0 9px}
.place{position:absolute;left:504px;top:0;width:76px;text-align:center;font:400 10px Arimo,Arial,sans-serif;color:var(--link-red)}
.place .pin{width:36px;height:36px;margin:36px auto 6px;border-radius:7px;background:linear-gradient(#f7e7a8,#d9c476);border:1px solid #bca85f}
.ribbon{position:absolute;left:582px;top:-8px;width:48px;height:122px}
.price{position:absolute;left:582px;top:33px;width:48px;text-align:center;color:#fff}
.price b{display:block;font:700 16px "Open Sans",Arial,sans-serif}
.price small{display:block;font-size:8px;line-height:9px}

/* footer */
.site-footer{position:absolute;left:0;top:903px;width:1000px;height:230px;background:linear-gradient(#2a2a2a,#1c1c1c)}
.foot-col{position:absolute;top:930px;font-size:10px;color:var(--footer-text);line-height:18.5px;white-space:nowrap}
.foot-col h4{font:400 12px "Open Sans",Arial,sans-serif;color:var(--yellow);margin-bottom:10px}
.foot-rule{position:absolute;top:925px;width:1px;height:140px;background:#3a3a3a}
.foot-line{left:87px;top:1081px;width:826px;height:1px;background:#3a3a3a}
.copyright{left:97px;top:1098px;font-size:10px;color:#aaa}
.social{position:absolute;top:1093px;width:22px;height:22px;border-radius:50%;background:#777}
</style>
</head>
<body>
<div class="page">

<header class="site-header">
  <div class="abs brand-mark"></div>
  <div class="abs brand-name">Step Outside</div>
  <div class="abs header-art" role="img" aria-label="Silhouette of a leaping dancer"></div>
  <div class="abs location-label">SELECT YOUR LOCATION:</div>
  <div class="abs location-select">ENTER YOUR CITY
    <span class="caret"><svg width="28" height="26"><path d="M9 11h10l-5 5z" fill="#fff"/></svg></span>
  </div>
</header>

<section class="search-band"></section>
<div class="abs search-title">OPTINAL SEARCH CRITERIA <span>HIDE</span></div>
<svg class="abs" style="left:592px;top:110px" width="46" height="42"><circle cx="18" cy="18" r="13" fill="#e8e8e8" stroke="#999" stroke-width="3"/><path d="M28 27l14 12" stroke="#ccc" stroke-width="5" stroke-linecap="round"/></svg>

<div class="abs course-box">
  <h3>SELECT YOUR COURSE :</h3>
  <div class="course-input">Search Courses By Keyword
    <svg width="13" height="13"><circle cx="5.5" cy="5.5" r="4" fill="none" stroke="#fff" stroke-width="1.6"/><path d="M8.5 8.5l3.5 3.5" stroke="#fff" stroke-width="1.8"/></svg>
  </div>
  <div class="course-crowd" role="img" aria-label="Silhouette of a cheering crowd"></div>
</div>

<div class="abs filter-panel"></div>
<div class="field" style="left:285px;top:162px;width:178px">Date From:</div>
<div class="field" style="left:472px;top:162px;width:178px">To:</div>
<div class="abs" style="left:285px;top:214px;width:368px;height:1px;background:#4a4a4a"></div>
<div class="abs panel-divider"></div>
<div class="field" style="left:688px;top:162px;width:213px">Any Time Of Day
  <svg style="position:absolute;right:0;top:0" width="32" height="32"><path d="M0 3v26" stroke="#aaa"/><path d="M10 13h12l-6 6z" fill="#333"/></svg>
</div>
<div class="abs day-row">
  <label>Mon<i></i></label><label>Tue<i></i></label><label>Wed<i></i></label><label>Thu<i></i></label><label>Fri<i></i></label><label>Sat<i></i></label><label>Sun<i></i></label>
  <label>ALL<i><svg style="position:absolute;left:1px;top:1px" width="8" height="8"><path d="M1 4l2 2 4-5" stroke="#3a9a2a" stroke-width="1.6" fill="none"/></svg></i></label>
</div>
<div class="abs filter-btn">FILTER
  <svg width="15" height="15"><circle cx="6" cy="6" r="4.5" fill="none" stroke="#fff" stroke-width="2"/><path d="M9.5 9.5l4 4" stroke="#fff" stroke-width="2.2"/></svg>
</div>

<aside>
  <div class="side-head" style="top:285px">Explore Courses &amp; Activities</div>
  <ul class="abs category-list">
    <li><span class="box">+</span>Visual Arts (32)</li>
    <li><span class="box">+</span>Cooking (14)</li>
    <li><span class="box">+</span>Health /Fitness (8)</li>
    <li><span class="box">+</span>Home /Life (19)</li>
    <li><span class="box">–</span>Languages (12)</li>
    <li class="sub">Danish (1)</li>
    <li class="sub">French (3)</li>
    <li class="sub">German (1)</li>
    <li class="sub">Mandarin (1)</li>
    <li class="sub">Portuges (1)</li>
    <li class="sub">Spanish (4)</li>
    <li><span class="box">+</span>Performing Arts (31)</li>
    <li><span class="box">+</span>Professional (28)</li>
    <li><span class="box">+</span>Tech /internet (5)</li>
    <li><span class="box">+</span>Arts And Sciences (9)</li>
  </ul>
  <div class="abs refine"></div>
  <div class="side-head" style="top:641px">Refine Search <small style="font-size:9px;font-weight:400">(Recammanded)</small></div>
  <div class="abs refine-label" style="top:677px">Age 18yrs+</div>
  <div class="abs slider" style="top:706px"><b></b></div>
  <div class="abs refine-label" style="top:730px">Max Price : $50</div>
  <div class="abs slider" style="top:757px"><b></b></div>
</aside>

<main>
  <div class="abs list-head">
    <span style="left:9px">Showing : All Courses &amp; Activities</span>
    <span style="left:440px">Schedule</span>
    <span style="left:517px">Location</span>
    <span style="left:592px">Price</span>
    <svg style="position:absolute;left:0;top:29px" width="643" height="5"><path d="M133 0h8l-4 4zM455 0h8l-4 4zM535 0h8l-4 4zM601 0h8l-4 4z" fill="#d9121b"/></svg>
  </div>

  <article class="card" style="top:332px">
    <div class="photo" role="img" aria-label="Photo of a salsa class" style="background:linear-gradient(135deg,#c9cdd4,#6f7888)"></div>
    <h2>SALSA PATTERNS</h2>
    <p>Lorem ipsum dolor sit amet, consectetur adipisicing elit, sed do eiusmod tempor incididunt ut labore et dolore magna aliqua. Ut enim ad minim veniam, quis nostrud exercitation ullamco laboris nisi ut do eiusmod tempor incididunt ut labore et dolore magna aliqua.</p>
    <span class="more">Read More ›</span>
    <div class="schedule">M&nbsp; 6PM<br>T&nbsp;&nbsp; 6PM<br>W&nbsp;5PM, 7PM<br>T&nbsp;&nbsp; -<br>F&nbsp;&nbsp; 7PM<br>S&nbsp;&nbsp; -<br>S&nbsp;&nbsp; -</div>
    <div class="place"><div class="pin" role="img" aria-label="Map marker"></div>South Bank</div>
    <svg class="ribbon" viewBox="0 0 48 122"><path d="M43 0l5 8H43z" fill="#7a0a0e"/><path d="M0 0h43v8h5v114L24 104 0 122z" fill="#d9121b"/></svg>
    <div class="price"><b>$15</b><small>SINGAL<br>SESSION</small></div>
  </article>

  <article class="card" style="top:469px">
    <div class="photo" role="img" aria-label="Photo of a ballroom dancing couple" style="background:linear-gradient(135deg,#e9e1d6,#a69684)"></div>
    <h2>BALLROOM DANCING FOR BEGINNERS</h2>
    <p>Lorem ipsum dolor sit amet, consectetur adipisicing elit, sed do eiusmod tempor incididunt ut labore et dolore magna aliqua. Ut enim ad minim veniam, quis nostrud exercitation ullamco laboris nisi ut do eiusmod tempor incididunt ut labore et dolore magna aliqua.</p>
    <span class="more">Read More ›</span>
    <div class="schedule">M&nbsp; 6PM<br>T&nbsp;&nbsp; 6PM<br>W&nbsp;5PM, 7PM<br>T&nbsp;&nbsp; -<br>F&nbsp;&nbsp; 7PM<br>S&nbsp;&nbsp; -<br>S&nbsp;&nbsp; -</div>
    <div class="place"><div class="pin" role="img" aria-label="Map marker"></div>Middle Park</div>
    <svg class="ribbon" viewBox="0 0 48 122"><path d="M43 0l5 8H43z" fill="#7a0a0e"/><path d="M0 0h43v8h5v114L24 104 0 122z" fill="#d9121b"/></svg>
    <div class="price"><b>$75</b><small>SINGAL<br>SESSION</small></div>
  </article>

  <article class="card" style="top:606px">
    <div class="photo" role="img" aria-label="Photo of two dancers in a studio" style="background:linear-gradient(135deg,#efe8df,#b29a7e)"></div>
    <h2>KICK YOUR BOOTY MAT</h2>
    <p>Lorem ipsum dolor sit amet, consectetur adipisicing elit, sed do eiusmod tempor incididunt ut labore et dolore magna aliqua. Ut enim ad minim veniam, quis nostrud exercitation ullamco laboris nisi ut do eiusmod tempor incididunt ut labore et dolore magna aliqua.</p>
    <span class="more">Read More ›</span>
    <div class="schedule">M&nbsp; 6PM<br>T&nbsp;&nbsp; 6PM<br>W&nbsp;5PM, 7PM<br>T&nbsp;&nbsp; -<br>F&nbsp;&nbsp; 7PM<br>S&nbsp;&nbsp; -<br>S&nbsp;&nbsp; -</div>
    <div class="place"><div class="pin" role="img" aria-label="Map marker"></div>Toorak</div>
    <svg class="ribbon" viewBox="0 0 48 122"><path d="M43 0l5 8H43z" fill="#7a0a0e"/><path d="M0 0h43v8h5v114L24 104 0 122z" fill="#d9121b"/></svg>
    <div class="price"><b>$35</b><small>SINGAL<br>SESSION</small></div>
  </article>

  <article class="card" style="top:744px">
    <div class="photo" role="img" aria-label="Photo of a tango couple" style="background:linear-gradient(135deg,#d8d2cc,#4a4240)"></div>
    <h2>ARGENTINE TANGO - INTERMIDEATE</h2>
    <p>Lorem ipsum dolor sit amet, consectetur adipisicing elit, sed do eiusmod tempor incididunt ut labore et dolore magna aliqua. Ut enim ad minim veniam, quis nostrud exercitation ullamco laboris nisi ut do eiusmod tempor incididunt ut labore et dolore magna aliqua.</p>
    <span class="more">Read More ›</span>
    <div class="schedule">M&nbsp; 6PM<br>T&nbsp;&nbsp; 6PM<br>W&nbsp;5PM, 7PM<br>T&nbsp;&nbsp; -<br>F&nbsp;&nbsp; 7PM<br>S&nbsp;&nbsp; -<br>S&nbsp;&nbsp; -</div>
    <div class="place"><div class="pin" role="img" aria-label="Map marker"></div>Windsor</div>
    <svg class="ribbon" viewBox="0 0 48 122"><path d="M43 0l5 8H43z" fill="#7a0a0e"/><path d="M0 0h43v8h5v114L24 104 0 122z" fill="#d9121b"/></svg>
    <div class="price"><b>$22</b><small>SINGAL<br>SESSION</small></div>
  </article>
</main>

<footer class="site-footer"></footer>
<div class="foot-col" style="left:109px"><h4>CUSTOMER</h4>Register<br>Login<br>Manage Booking</div>
<div class="foot-rule" style="left:254px"></div>
<div class="foot-col" style="left:301px"><h4>BUSINESSES</h4>Register<br>Login</div>
<div class="foot-rule" style="left:418px"></div>
<div class="foot-col" style="left:475px"><h4>COURSES</h4>Link 1<br>Link 2<br>Link 3</div>
<div class="foot-rule" style="left:584px"></div>
<div class="foot-col" style="left:638px"><h4>ACTIVITY</h4>Link 1<br>Link 2<br>Link 3</div>
<div class="foot-rule" style="left:747px"></div>
<div class="foot-col" style="left:777px"><h4>CONTACT US</h4>Lorem ipsum dolor sit,<br>consectetu adipisicing elit,<br>Pin: 123456<br><br>
  <svg width="12" height="10" style="vertical-align:-1px"><path d="M1 3q5-4 10 0v2H8V3.5H4V5H1zM3 6h6l1 4H2z" fill="#aaa"/></svg> Ph- 1234 56789</div>
<div class="abs foot-line"></div>
<div class="abs copyright">Copyright © &nbsp;2011 Step Outside. All Right Reserved.</div>
<div class="social" style="left:828px"></div>
<div class="social" style="left:855px"></div>
<div class="social" style="left:883px"></div>

</div>
</body>
</html>
```